Design a landing page

We have a logo, we have colours in mind. What we need is to create a typical one-page landing page that would look nicely on both PC and mobile devices/tablets.

Typical layout - logo top left, top right - shop/client area buttons (links will open to different websites), informational area in the middle - image on the left + text on the right then image on the right + text on the left etc., then text links at the bottom (T&S, Cookie policy, privacy policy etc.).

Page must have cookie notification as per EU law.

We will also need help in preparing photos/images (up to 8) for the website.

End result should be either a Wordpress theme (preferred - so we can install it from wordpress control panel) or HTML/CSS page source. All scripts/images/files should be included - no external links to js/image libraries please.

The photo of the device attached. Primary users will be home users with placement on the ceiling, Minority of users will be business/commercial users with wall placements. Device is meant to monitor climat in the premises (Temperature, humidity, dew point) and alert users if readings are not within allowed range.

Need extra days to review

Industry/Entity Type

Microclimate Monitoring in premises

Coding

Coded - Design and coding required

Number of Pages Required

1 page

Colors
0054AA
0677BA
7BADD7
CADEEF
E8F1F8
0094D4
00A9DD
6FCCEA
C7EBF8
E9F6FB

Requirements
Must have
• White background, layout as described unless better option offered and accepted. Must have cookie warning.

```html
<!DOCTYPE html>
<html lang="en">
<head>
<meta charset="utf-8">
<title>Climora – Smart Climate Monitoring</title>
<link rel="stylesheet" href="https://fonts.googleapis.com/css2?family=Poppins:wght@300;400;500;600;700&display=swap">
<style>
:root{
  --navy:#0054AA;--blue:#0677BA;--sky:#7BADD7;--mist:#CADEEF;--ice:#E8F1F8;
  --cyan:#0094D4;--aqua:#00A9DD;--teal:#6FCCEA;--pale:#C7EBF8;--frost:#E9F6FB;
  --ink:#12305a;--text:#3a4a60;--white:#fff;
}
*{box-sizing:border-box;margin:0;padding:0}
html,body{width:1200px;height:4280px;overflow:hidden}
body{font-family:"Poppins",sans-serif;color:var(--text);background:var(--white);position:relative}
section,header,footer{position:absolute;left:0;width:1200px}
.img{position:absolute;border-radius:6px}
.btn{display:inline-block;font-size:13px;font-weight:500;padding:7px 20px;border-radius:3px;text-decoration:none}
.btn-solid{background:var(--aqua);color:#fff}
.btn-line{border:1.5px solid var(--aqua);color:var(--aqua);background:#fff}
.ticks{list-style:none}
.ticks li{position:relative;padding-left:36px}
.ticks li svg{position:absolute;left:0;top:50%;transform:translateY(-50%)}

/* header */
.site-header{top:0;height:120px;z-index:3}
.brand{position:absolute;left:40px;top:50px;font-size:34px;font-weight:700;color:var(--ink);letter-spacing:1px}
.toplinks{position:absolute;right:60px;top:24px;display:flex;gap:12px;align-items:center;font-size:13px;color:var(--ink)}
.toplinks .shop{background:var(--aqua);color:#fff;padding:3px 12px;border-radius:3px}
.dot{width:14px;height:14px;border-radius:50%;background:var(--aqua);display:inline-block}
.nav{position:absolute;left:600px;top:66px;width:580px;height:36px;background:var(--sky);display:flex}
.nav a{flex:1;color:#fff;font-size:15px;font-weight:500;text-align:center;line-height:36px;text-decoration:none}
.nav a.active{background:var(--navy)}

/* hero */
.hero{top:0;height:860px;background:linear-gradient(100deg,#f3f8fc 0%,var(--ice) 50%,var(--pale) 100%)}
.hero-photo{left:560px;top:120px;width:640px;height:720px;border-radius:0;background:linear-gradient(120deg,var(--ice),var(--mist) 55%,var(--sky))}
.hero h1{position:absolute;left:88px;top:288px;font-size:40px;font-weight:600;color:var(--ink);letter-spacing:.5px}
.hero h1 span{color:var(--aqua)}
.hero .tag{position:absolute;left:88px;top:340px;font-size:30px;color:var(--ink);letter-spacing:5px;font-weight:400}
.hero p{position:absolute;left:88px;top:392px;width:500px;font-size:17px;line-height:1.5;color:var(--text)}
.hero .ctas{position:absolute;left:88px;top:500px;display:flex;gap:20px}
.chips{position:absolute;left:88px;top:648px;display:flex;gap:16px}
.chip{background:#fff;border-radius:20px;padding:8px 18px;font-size:13px;color:var(--ink);display:flex;gap:8px;align-items:center;box-shadow:0 2px 8px rgba(0,84,170,.12)}

/* why */
.why{top:860px;height:600px;background:linear-gradient(180deg,#fff,var(--ice))}
.why-photo{left:100px;top:135px;width:460px;height:360px;background:linear-gradient(135deg,#d8d4cc,#eeebe6 60%,#c9c3b9)}
.why h2{position:absolute;left:620px;top:176px;font-size:30px;font-weight:600;color:var(--ink);letter-spacing:1px}
.why p{position:absolute;left:620px;top:222px;width:520px;font-size:19px;line-height:1.5;color:var(--ink)}
.why ul{position:absolute;left:620px;top:326px;font-size:15px;line-height:2}
.why .btn{position:absolute;left:632px;top:406px}

/* home */
.home{top:1460px;height:590px;background:linear-gradient(180deg,var(--ice),var(--frost))}
.home h2{position:absolute;left:92px;top:130px;font-size:32px;font-weight:400;color:var(--ink);line-height:1.35;letter-spacing:1px}
.home h2 b{font-weight:600}
.home ul{position:absolute;left:92px;top:230px;font-size:24px;line-height:1.6;color:var(--ink)}
.home-photo{left:640px;top:84px;width:340px;height:320px;background:linear-gradient(135deg,#e9edf1,#b9c6d2 50%,#6d86a0)}
.cards{position:absolute;left:88px;top:468px;display:flex;gap:24px}
.fcard{width:212px;height:100px;background:#fff;border:1px solid var(--mist);border-radius:4px;padding:16px 14px;display:flex;gap:10px}
.fcard h4{font-size:14px;font-weight:600;color:var(--ink)}
.fcard p{font-size:12px;line-height:1.35;color:var(--text)}

/* gallery */
.gallery{top:2050px;height:550px;display:grid;grid-template-columns:1fr 1fr 1fr;grid-template-rows:1fr 1fr}
.gallery div{position:static;border-radius:0}
.g1{background:linear-gradient(135deg,#3a4455,#727d8c)}
.g2{background:linear-gradient(135deg,#e3e0da,#c2b89a 60%,#d5b13c)}
.g3{background:linear-gradient(135deg,#f3f4f6,#cfd6de)}
.g4{background:linear-gradient(135deg,#4a5c74,#8aa0b8)}
.g5{background:linear-gradient(135deg,#8a5a3a,#c69468)}
.g6{background:linear-gradient(135deg,#9aa9b8,#d6dde4)}

/* business */
.business{top:2600px;height:280px;background:linear-gradient(180deg,#fff,var(--ice))}
.business h2{position:absolute;left:88px;top:66px;font-size:26px;font-weight:600;color:var(--ink);letter-spacing:1px}
.business ul{position:absolute;top:112px;font-size:24px;line-height:1.55;color:var(--ink)}
.business .col1{left:88px}.business .col2{left:620px}

/* how */
.how{top:2880px;height:640px;background:linear-gradient(180deg,var(--frost),var(--pale))}
.how h2{position:absolute;left:88px;top:66px;font-size:38px;font-weight:600;color:var(--cyan);letter-spacing:1px}
.how-photo{left:84px;top:260px;width:400px;height:340px;background:linear-gradient(135deg,#6b4a30,#a77b54 55%,#d9c3a6)}
.steps{position:absolute;left:528px;top:256px;display:grid;grid-template-columns:300px 300px;gap:40px 44px}
.step{background:#fff;border-radius:4px;padding:18px 16px;height:150px;display:flex;gap:12px;box-shadow:0 3px 10px rgba(0,84,170,.1)}
.step h4{font-size:16px;font-weight:600;color:var(--ink)}
.step p{font-size:12.5px;line-height:1.45;margin-top:4px}

/* cta */
.cta{top:3520px;height:440px;background:linear-gradient(180deg,var(--pale),#fff 30%);text-align:center}
.cta h2{margin-top:130px;font-size:35px;font-weight:600;color:var(--navy)}
.cta p{font-size:31px;color:var(--ink);line-height:1.45;margin-top:10px}
.cta .btn{margin-top:26px;font-size:18px;padding:10px 40px;background:var(--blue)}

/* footer */
.site-footer{top:3960px;height:240px;background:var(--cyan);color:#fff}
.fbrand{position:absolute;left:88px;top:40px;width:120px;height:60px;background:#fff;color:var(--ink);font-size:19px;font-weight:700;text-align:center;line-height:60px;border-radius:2px}
.fabout{position:absolute;left:220px;top:44px;width:160px;font-size:11px;line-height:1.4}
.flinks{position:absolute;left:620px;top:56px;display:grid;grid-template-columns:120px 120px 120px;font-size:17px;line-height:1.5}
.follow{position:absolute;left:1036px;top:56px;font-size:17px}
.follow .dots{display:flex;gap:10px;margin-top:8px}
.follow .dot{background:#fff}
.fbottom{position:absolute;left:0;top:160px;width:1200px;height:80px;border-top:1px solid rgba(255,255,255,.35);background:var(--blue);font-size:13px}
.fbottom .copy{position:absolute;left:88px;top:26px}
.fbottom .legal{position:absolute;left:620px;top:26px}

/* cookie */
.cookie{top:4200px;height:80px;background:var(--ice);border-top:2px solid var(--mist)}
.cookie p{position:absolute;left:120px;top:18px;width:560px;font-size:13px;line-height:1.45;color:var(--ink)}
.cookie p a{color:var(--navy);font-weight:600}
.cookie .icon{position:absolute;left:88px;top:22px;width:20px;height:20px;border-radius:50%;background:var(--cyan)}
.cookie .actions{position:absolute;left:680px;top:22px;display:flex;gap:14px}
.cookie .btn{font-size:14px;padding:6px 16px}
.cookie .accept{background:var(--navy);color:#fff}
.cookie .essential{background:var(--blue);color:#fff}
</style>
</head>
<body>

<section class="hero">
  <div class="img hero-photo" role="img" aria-label="Smiling woman holding a phone showing climate readings beside a ceiling-mounted sensor"></div>
  <h1><span>SMART CLIMATE</span> MONITORING</h1>
  <div class="tag">Complete Peace of Mind</div>
  <p>Real-time temperature, humidity and dew point monitoring for homes and commercial spaces – with instant alerts when conditions go beyond safe limits.</p>
  <div class="ctas"><a class="btn btn-solid" href="#">BUY NOW</a><a class="btn btn-line" href="#">CLIENT AREA</a></div>
  <div class="chips">
    <span class="chip"><svg width="14" height="14" viewBox="0 0 14 14"><rect x="5" y="1" width="4" height="9" rx="2" fill="none" stroke="#0094D4" stroke-width="1.5"/><circle cx="7" cy="11" r="2.5" fill="#0094D4"/></svg>Temperature</span>
    <span class="chip"><svg width="14" height="14" viewBox="0 0 14 14"><path d="M7 1C5 5 3 7 3 9a4 4 0 0 0 8 0c0-2-2-4-4-8z" fill="#0094D4"/></svg>Humidity</span>
    <span class="chip"><svg width="14" height="14" viewBox="0 0 14 14"><circle cx="7" cy="7" r="5" fill="none" stroke="#0094D4" stroke-width="1.5"/><circle cx="7" cy="7" r="2" fill="#0094D4"/></svg>Dew point</span>
  </div>
</section>

<header class="site-header">
  <div class="brand">CLIMORA</div>
  <div class="toplinks"><span>Shop</span><span>·</span><span>Client Area</span><span class="shop">SHOP ▾</span><span class="dot"></span><span class="dot"></span><span class="dot"></span><span class="dot"></span></div>
  <nav class="nav"><a class="active" href="#">HOME</a><a href="#">ABOUT US</a><a href="#">PRODUCTS</a><a href="#">SERVICES</a><a href="#">CONTACT US</a></nav>
</header>

<section class="why">
  <div class="img why-photo" role="img" aria-label="Hand fitting a round climate sensor to a ceiling"></div>
  <h2>WHY MONITORING MATTERS</h2>
  <p>Temperature, humidity and dew point monitoring are crucial for maintaining optimal indoor environments and preventing damage.</p>
  <ul class="ticks">
    <li><svg width="16" height="16" viewBox="0 0 16 16"><circle cx="8" cy="8" r="8" fill="#0094D4"/><path d="M4.5 8.2l2.3 2.3 4.7-4.8" stroke="#fff" stroke-width="1.8" fill="none"/></svg>Lorem ipsum dolor sit amet, consectetur</li>
    <li><svg width="16" height="16" viewBox="0 0 16 16"><circle cx="8" cy="8" r="8" fill="#0094D4"/><path d="M4.5 8.2l2.3 2.3 4.7-4.8" stroke="#fff" stroke-width="1.8" fill="none"/></svg>eiusmod tempor incididunt ut labore et dolore</li>
  </ul>
  <a class="btn btn-solid" href="#">Read More</a>
</section>

<section class="home">
  <h2>PERFECT FOR <b>HOME CELLING<br>INSTALLATION</b></h2>
  <ul class="ticks">
    <li><svg width="22" height="20" viewBox="0 0 22 20"><path d="M2 10l6 6L20 3" stroke="#0054AA" stroke-width="3" fill="none"/></svg>Minimal design</li>
    <li><svg width="22" height="20" viewBox="0 0 22 20"><path d="M2 10l6 6L20 3" stroke="#0054AA" stroke-width="3" fill="none"/></svg>Discrete celling placement</li>
    <li><svg width="22" height="20" viewBox="0 0 22 20"><path d="M2 10l6 6L20 3" stroke="#0054AA" stroke-width="3" fill="none"/></svg>Mobile or dashboad alerts</li>
  </ul>
  <div class="img home-photo" role="img" aria-label="Black hexagonal sensor on a ceiling beside a bright living room"></div>
  <div class="cards">
    <div class="fcard"><svg width="22" height="22" viewBox="0 0 22 22"><rect x="3" y="3" width="16" height="16" rx="3" fill="none" stroke="#0094D4" stroke-width="2"/></svg><div><h4>Minimal Design</h4><p>Temperature fluctuations testing in ceiling level</p></div></div>
    <div class="fcard"><svg width="22" height="22" viewBox="0 0 22 22"><path d="M11 2v18M2 11h18" stroke="#0094D4" stroke-width="2"/></svg><div><h4>Discretes</h4><p>Ceiling placement in cooling issues</p></div></div>
    <div class="fcard"><svg width="22" height="22" viewBox="0 0 22 22"><rect x="6" y="2" width="10" height="18" rx="2" fill="none" stroke="#0094D4" stroke-width="2"/></svg><div><h4>Mobile</h4><p>Dashboard alerts</p></div></div>
    <div class="fcard"><svg width="22" height="22" viewBox="0 0 22 22"><path d="M11 2C8 8 5 11 5 14a6 6 0 0 0 12 0c0-3-3-6-6-12z" fill="#0094D4"/></svg><div><h4>Dew point</h4><p>Helps prevent condensation</p></div></div>
  </div>
</section>

<section class="gallery">
  <div class="g1" role="img" aria-label="Black hexagonal sensor on a warehouse wall"></div>
  <div class="g2" role="img" aria-label="White hexagonal sensor above yellow and black hazard tape"></div>
  <div class="g3" role="img" aria-label="White sensor on a bright wall"></div>
  <div class="g4" role="img" aria-label="Industrial warehouse aisle with shelving"></div>
  <div class="g5" role="img" aria-label="Storage room with wooden floor and racks"></div>
  <div class="g6" role="img" aria-label="Small white sensor placed on a table"></div>
</section>

<section class="business">
  <h2>RELIABLE MONITORING FOR BUSINESSES</h2>
  <ul class="ticks col1">
    <li><svg width="22" height="20" viewBox="0 0 22 20"><path d="M2 10l6 6L20 3" stroke="#0054AA" stroke-width="3" fill="none"/></svg>Real-Time Data Tracking</li>
    <li><svg width="22" height="20" viewBox="0 0 22 20"><path d="M2 10l6 6L20 3" stroke="#0054AA" stroke-width="3" fill="none"/></svg>Instant Alert Notifications</li>
    <li><svg width="22" height="20" viewBox="0 0 22 20"><path d="M2 10l6 6L20 3" stroke="#0054AA" stroke-width="3" fill="none"/></svg>Accurate Dew Point Monitoring</li>
  </ul>
  <ul class="ticks col2">
    <li><svg width="22" height="20" viewBox="0 0 22 20"><path d="M2 10l6 6L20 3" stroke="#0054AA" stroke-width="3" fill="none"/></svg>Energy Efficient Operation</li>
    <li><svg width="22" height="20" viewBox="0 0 22 20"><path d="M2 10l6 6L20 3" stroke="#0054AA" stroke-width="3" fill="none"/></svg>Clean &amp; Modern Design</li>
    <li><svg width="22" height="20" viewBox="0 0 22 20"><path d="M2 10l6 6L20 3" stroke="#0054AA" stroke-width="3" fill="none"/></svg>Maintain Regulatory Alerts</li>
  </ul>
</section>

<section class="how">
  <h2>HOW IT WORKS</h2>
  <div class="img how-photo" role="img" aria-label="Round sensor on a wooden shelf in a warm-toned room"></div>
  <div class="steps">
    <div class="step"><svg width="26" height="26" viewBox="0 0 26 26"><rect x="4" y="4" width="18" height="18" rx="3" fill="#0094D4"/></svg><div><h4>Install</h4><p>Monitor temperature or volume, monitor online tools, alerts.</p></div></div>
    <div class="step"><svg width="26" height="26" viewBox="0 0 26 26"><path d="M13 3C10 9 7 12 7 16a6 6 0 0 0 12 0c0-4-3-7-6-13z" fill="#0094D4"/></svg><div><h4>Connect</h4><p>Get WiFi &amp; Ethernet connection maintained on cable and routers.</p></div></div>
    <div class="step"><svg width="26" height="26" viewBox="0 0 26 26"><path d="M4 18l6-6 4 4 8-8" stroke="#0094D4" stroke-width="2.5" fill="none"/></svg><div><h4>Set Range</h4><p>Accurate dew point monitoring. Wireless operation and security.</p></div></div>
    <div class="step"><svg width="26" height="26" viewBox="0 0 26 26"><path d="M13 4a6 6 0 0 0-6 6v5l-2 3h16l-2-3v-5a6 6 0 0 0-6-6z" fill="#0094D4"/><circle cx="13" cy="21" r="2" fill="#0094D4"/></svg><div><h4>Get Alerts</h4><p>Maintain instant alerts when switching becomes to prevent threshold rivers.</p></div></div>
  </div>
</section>

<section class="cta">
  <h2>TAKE CONTROL OF YOUR INDOOR CLIMATE TODAY</h2>
  <p><b>Don't wait for damage</b> to happen.<br>Monitor it before it becomes a problem.</p>
  <a class="btn btn-solid" href="#">BUY NOW</a>
</section>

<footer class="site-footer">
  <div class="fbrand">CLIMORA</div>
  <div class="fabout">Precision climate intelligence for smarter, safer business environments.</div>
  <div class="flinks"><span>Home</span><span>Services</span><span>News &amp; Events</span><span>About Us</span><span>Products</span><span>Contact Us</span></div>
  <div class="follow">Follow us<div class="dots"><span class="dot"></span><span class="dot"></span><span class="dot"></span><span class="dot"></span></div></div>
  <div class="fbottom"><span class="copy">©2026 Climora. All rights reserved.</span><span class="legal">Privacy Policies | Terms &amp; Conditions | Cookies | Legal | Accessibility</span></div>
</footer>

<section class="cookie">
  <span class="icon"></span>
  <p>This site uses cookies. Visit our <a href="#">cookies policy page</a> or click the link in any footer for more information and to change your preferences.</p>
  <div class="actions"><a class="btn accept" href="#">Accept all cookies</a><a class="btn essential" href="#">Accept only essential cookies</a></div>
</section>

</body>
</html>
```